Finance Flyer/ brouchure Design

I would a finance flyer/ brouchure deisgned detailing the services that we offer as per the below.
Lending & Leasing
General Insurance
Risk Insurance
Wealth Planning
Commercial, Equipment & Asset Finance
I would also like the brouchure to state that 'we have access to over 35 lenders', 'Our services are free to you', 'We will find you the best deal & make it easy for you'.
I would like a spot on the flyer/ brouchure where I can place a picture of the local finance broker and a short bio on them.
I would like to be able to come back to the person ultimately chosen to design a suite of flyers.

Target Market(s)

My target auidience are families, aged between 30 & 50 with children.
I would like the flyer to appear professional but friendly and to work with the colours of my logo.

Industry/Entity Type

Finance

Font styles to use
Serif

Colors

Designer to choose colors to be used in the design.

Requirements
Must have
• Be friendly & inviting
• Work with the colours of my logo
• Call to action - 'Call us today on 1300 482 615'
• Must have a Contact us section including the following
• Phone number- 1300 482 615
• Location- Brisbane & surrounds
• Email- Moira@tallowbq.com.au
• Website- www.tallowbq.com.au
• Facebook- www.facebook.com/tallowmonetary

```html
<!DOCTYPE html>
<html lang="en">
<head>
<meta charset="utf-8">
<title>Tallow Monetary Solutions — Brochure Spread</title>
<link href="https://fonts.googleapis.com/css2?family=Open+Sans:wght@400;600;700&display=swap" rel="stylesheet">
<style>
  :root {
    --teal: #23505e;
    --green: #8cc152;
    --green-light: #a6d16a;
    --paper: #f1f3f6;
    --paper-shade: #dfe3e8;
    --ink: #2b3a42;
    --stage: #3a3d42;
    --portrait: #c9cfd6;
  }
  * { margin: 0; padding: 0; box-sizing: border-box; }
  html, body { width: 1200px; height: 789px; overflow: hidden; background: var(--stage); }
  body { font-family: "Open Sans", Arial, sans-serif; color: var(--ink); }

  .spread { position: absolute; left: 80px; top: 26px; width: 1040px; height: 736px; display: flex; box-shadow: 0 10px 30px rgba(0,0,0,.45); }
  .page { position: relative; width: 520px; height: 736px; overflow: hidden; }
  .page--back { background: linear-gradient(120deg, #f6f7f9 0%, var(--paper) 55%, var(--paper-shade) 100%); }
  .page--front { background: linear-gradient(240deg, #f7f8fa 0%, var(--paper) 60%, var(--paper-shade) 100%); }
  .bands, .photo { position: absolute; inset: 0; width: 100%; height: 100%; }

  .services { position: absolute; left: 0; top: 36px; }
  .services__title { display: inline-block; background: var(--teal); color: #fff; font-size: 22px; font-weight: 400; padding: 4px 46px 4px 34px; clip-path: polygon(0 0, 100% 0, 88% 100%, 0 100%); }
  .services__list { list-style: none; margin: 10px 0 0 44px; }
  .services__list li { font-size: 16px; line-height: 25px; color: var(--ink); }
  .services__list li::before { content: "➤"; font-size: 11px; color: var(--teal); margin-right: 10px; vertical-align: 2px; }

  .broker { position: absolute; left: 44px; top: 224px; display: flex; gap: 12px; width: 330px; }
  .broker__photo { width: 76px; height: 76px; flex: none; background: linear-gradient(160deg, var(--portrait), #9fa8b2); border: 3px solid var(--green); }
  .broker__title { font-size: 14px; font-weight: 700; color: var(--teal); line-height: 18px; }
  .broker__bio { font-size: 11.5px; line-height: 16px; margin-top: 3px; }

  .brand { position: absolute; display: flex; align-items: center; gap: 10px; }
  .brand__mark { width: 18px; height: 18px; background: var(--green); flex: none; }
  .brand__name { font-size: 22px; font-weight: 700; color: var(--teal); line-height: 1.1; }
  .page--back .brand { left: 60px; top: 316px; }
  .page--back .brand__name { font-size: 18px; }
  .page--front .brand { right: 40px; top: 468px; }

  .contact { position: absolute; left: 40px; bottom: 24px; width: 300px; }
  .contact__title { font-size: 24px; font-weight: 400; border-bottom: 1px solid var(--ink); padding-bottom: 2px; margin-bottom: 6px; }
  .contact__row { display: flex; align-items: center; gap: 10px; font-size: 13px; line-height: 22px; }
  .contact__row--lg { font-size: 19px; line-height: 26px; }
  .contact__icon { width: 16px; height: 16px; flex: none; }

  .promises { position: absolute; right: 40px; top: 530px; width: 290px; list-style: none; text-align: right; }
  .promises li { font-size: 13px; line-height: 19px; color: var(--ink); }
  .promises li::after { content: " ✓"; color: var(--green); font-weight: 700; }
  .cta { position: absolute; right: 40px; top: 612px; font-size: 16px; font-weight: 700; color: var(--teal); }

  .web-tag { position: absolute; left: 0; bottom: 36px; background: var(--green); color: #fff; font-size: 17px; font-weight: 600; padding: 8px 40px 8px 30px; }
</style>
</head>
<body>
  <main class="spread">
    <section class="page page--back">
      <svg class="bands" viewBox="0 0 520 736" aria-hidden="true">
        <polygon points="0,520 200,372 520,345 520,356 206,384 0,534" fill="var(--teal)"/>
        <polygon points="0,548 214,392 520,366 520,402 226,428 0,600" fill="var(--green)"/>
        <polygon points="296,736 520,566 520,578 312,736" fill="var(--teal)"/>
        <polygon points="326,736 520,590 520,630 378,736" fill="var(--green)"/>
      </svg>

      <div class="services">
        <h2 class="services__title">What we do?</h2>
        <ul class="services__list">
          <li>Lending &amp; Leasing</li>
          <li>General Insurance</li>
          <li>Risk Insurance</li>
          <li>Wealth Planning</li>
          <li>Commercial, Equipment &amp; Asset Finance</li>
        </ul>
      </div>

      <div class="broker">
        <div class="broker__photo" role="img" aria-label="Portrait photo of the local finance broker"></div>
        <div>
          <h3 class="broker__title">Meet your local broker</h3>
          <p class="broker__bio">Helping Brisbane families find the right loan and cover for over ten years, with friendly advice at every step.</p>
        </div>
      </div>

      <div class="brand">
        <span class="brand__mark"></span>
        <span class="brand__name">Tallow Monetary<br>Solutions</span>
      </div>

      <div class="contact">
        <h3 class="contact__title">Contact us</h3>
        <div class="contact__row contact__row--lg">
          <svg class="contact__icon" viewBox="0 0 16 16"><path d="M8 1a5 5 0 0 0-5 5c0 4 5 9 5 9s5-5 5-9a5 5 0 0 0-5-5zm0 7a2 2 0 1 1 0-4 2 2 0 0 1 0 4z" fill="var(--ink)"/></svg>
          Brisbane &amp; surrounds
        </div>
        <div class="contact__row contact__row--lg">
          <svg class="contact__icon" viewBox="0 0 16 16"><path d="M4 1l3 3-2 2c1 2 3 4 5 5l2-2 3 3-2 3C7 15 1 9 1 3z" fill="var(--ink)"/></svg>
          1300 482 615
        </div>
        <div class="contact__row">
          <svg class="contact__icon" viewBox="0 0 16 16"><rect x="1" y="3" width="14" height="10" rx="1" fill="var(--ink)"/><path d="M1 4l7 5 7-5" stroke="#fff" fill="none"/></svg>
          Moira@tallowbq.com.au
        </div>
        <div class="contact__row">
          <svg class="contact__icon" viewBox="0 0 16 16"><circle cx="8" cy="8" r="7" fill="none" stroke="var(--ink)" stroke-width="1.5"/><path d="M1 8h14M8 1c-3 3-3 11 0 14M8 1c3 3 3 11 0 14" stroke="var(--ink)" fill="none"/></svg>
          www.tallowbq.com.au
        </div>
        <div class="contact__row">
          <svg class="contact__icon" viewBox="0 0 16 16"><circle cx="8" cy="8" r="7" fill="var(--ink)"/></svg>
          www.facebook.com/tallowmonetary
        </div>
      </div>
    </section>

    <section class="page page--front">
      <svg class="photo" viewBox="0 0 520 736">
        <defs>
          <linearGradient id="photoTone" x1="0" y1="0" x2="1" y2="1">
            <stop offset="0" stop-color="#e9dccb"/>
            <stop offset=".5" stop-color="#9a7a63"/>
            <stop offset="1" stop-color="#b88d5e"/>
          </linearGradient>
        </defs>
        <polygon role="img" aria-label="Photo of a couple meeting a finance broker and signing papers at a table" points="0,0 520,0 520,330 300,322 110,470 0,470" fill="url(#photoTone)"/>
        <polygon points="0,470 110,470 300,322 520,330 520,342 306,334 116,482 0,482" fill="var(--teal)"/>
        <polygon points="0,482 116,482 306,334 520,342 520,382 330,372 130,540 0,560" fill="var(--green)"/>
        <polygon points="0,578 240,402 520,412 520,422 246,414 0,592" fill="var(--teal)"/>
        <polygon points="0,600 250,424 520,434 520,452 262,444 0,640" fill="var(--green-light)"/>
      </svg>

      <div class="brand">
        <span class="brand__mark"></span>
        <span class="brand__name">Tallow Monetary<br>Solutions</span>
      </div>

      <ul class="promises">
        <li>We have access to over 35 lenders</li>
        <li>Our services are free to you</li>
        <li>We will find you the best deal &amp; make it easy for you</li>
      </ul>

      <p class="cta">Call us today on 1300 482 615</p>

      <div class="web-tag">www.tallowbq.com.au</div>
    </section>
  </main>
</body>
</html>
```